Personal Trainer. Corvane PT. Needs poster to attract clients.

I need a poster to attract clients to my business Corvane PT.
The demographic I am targeting is 30-45 year old overweight women and men. I would like some gym pictures incorporated. (these should not be pics of athletes/super fit body types)These are up to you. Please note my target market as super fit models would not be appropriate.
I am fond of the black background but I am open to change.

I wanted my contact details to be
Phone number- 0437 802 615
and
Facebook- Corvane PT.
No email, website or street address please
I would like a small picture of myself near the contact details but do not want my photo to be a feature.

Attached is my old poster design.
****PLEASE NOTE CHANGES ABOVE****

Target Market(s)

Both overweight women and men 30-45 years old

Industry/Entity Type

Business

Requirements
Should not have
• Street address
• Web address
• Pics of super fit athletes

```html
<!DOCTYPE html>
<html lang="en">
<head>
<meta charset="UTF-8">
<title>Corvane PT – Poster</title>
<link href="https://fonts.googleapis.com/css2?family=Antonio:wght@100;400;700&display=swap" rel="stylesheet">
<style>
  :root {
    --canvas: #ffffff;
    --poster-dark: #2b2828;
    --poster-mid: #3d3837;
    --brand-yellow: #ffe01b;
    --brand-blue: #0a8ad6;
    --photo-light: #e9e9e9;
    --photo-grey: #8c8c8c;
    --ink-dark: #1a1a1a;
  }
  * { margin: 0; padding: 0; box-sizing: border-box; }
  html, body {
    width: 1200px; height: 1000px; overflow: hidden;
    background: var(--canvas);
    font-family: "Antonio", "Arial Narrow", sans-serif;
  }
  .poster {
    position: absolute; left: 256px; top: 18px;
    width: 675px; height: 954px;
    overflow: hidden;
    background: var(--poster-dark);
  }
  .poster-backdrop {
    position: absolute; inset: 0;
    background: radial-gradient(ellipse at 55% 40%, var(--poster-mid) 0%, var(--poster-dark) 70%);
  }
  .brand-name {
    position: absolute; left: 16px; top: 30px;
    font-weight: 700; font-size: 96px; line-height: 1;
    letter-spacing: 12px; color: var(--brand-yellow);
    white-space: nowrap;
  }
  .brand-rule {
    position: absolute; left: 16px; top: 156px;
    width: 543px; height: 3px; background: var(--brand-blue);
  }
  .tagline, .motto, .fun-line {
    position: absolute; color: var(--brand-yellow);
    font-weight: 400; text-transform: uppercase;
  }
  .tagline { left: 26px; top: 168px; font-size: 46px; line-height: 1; white-space: nowrap; }
  .motto { left: 26px; top: 266px; font-size: 46px; line-height: 1; white-space: nowrap; }
  .motto-word {
    position: absolute; left: 30px; top: 299px;
    font-weight: 100; font-size: 180px; line-height: 1;
    color: var(--brand-blue); letter-spacing: 6px;
    white-space: nowrap;
  }
  .fun-line {
    left: 290px; top: 602px; width: 295px;
    font-size: 52px; line-height: 70px; text-align: center;
  }
  .photo-circle {
    position: absolute; border-radius: 50%;
  }
  .photo-equipment {
    left: 384px; top: 232px; width: 304px; height: 304px;
    border: 4px solid var(--brand-yellow);
    background: linear-gradient(160deg, var(--photo-light) 0%, #d8dde4 55%, #2f5fae 75%, #e3e3e3 100%);
  }
  .photo-kettlebell {
    left: -96px; top: 497px; width: 370px; height: 370px;
    border: 4px solid var(--brand-blue);
    background: linear-gradient(180deg, #6e6e6e 0%, #b0b0b0 30%, #f2d21a 50%, #e7c30f 100%);
  }
  .photo-trainer {
    left: 521px; top: 795px; width: 134px; height: 134px;
    border: 4px solid var(--brand-yellow);
    background: linear-gradient(180deg, #d6d6d6 0%, var(--photo-grey) 60%, #2a2a2a 100%);
  }
  .contact-row {
    position: absolute; left: 60px; top: 840px;
    display: flex; align-items: center; gap: 14px;
    color: var(--brand-yellow); font-size: 30px; white-space: nowrap;
  }
  .contact-icon {
    width: 46px; height: 46px; border-radius: 50%;
    background: var(--brand-yellow);
    display: flex; align-items: center; justify-content: center;
  }
  .contact-gap { width: 14px; }
</style>
</head>
<body>
  <main class="poster">
    <div class="poster-backdrop" role="img" aria-label="Dim photo of a cheerful group of everyday gym members with exercise balls"></div>

    <div class="brand-name">CORVANE PT</div>
    <div class="brand-rule"></div>

    <p class="tagline">Change your life today</p>
    <p class="motto">Train - Live - Be</p>
    <p class="motto-word">WELL</p>

    <div class="photo-circle photo-equipment" role="img" aria-label="Photo of blue hand dumbbells beside a bathroom scale"></div>
    <div class="photo-circle photo-kettlebell" role="img" aria-label="Photo of a yellow kettlebell in front of training shoes"></div>

    <p class="fun-line">Fitness has<br>never been<br>such fun</p>

    <div class="contact-row">
      <span class="contact-icon" aria-hidden="true"></span>
      <span class="contact-social">Corvane PT</span>
      <span class="contact-gap"></span>
      <span class="contact-icon" aria-hidden="true">
        <svg width="26" height="26" viewBox="0 0 24 24">
          <path fill="#1a1a1a" d="M6.6 2.5c.6-.4 1.4-.3 1.8.3l2.1 3.2c.4.6.3 1.3-.2 1.8l-1.5 1.3c.9 2 2.5 3.8 4.3 5l1.4-1.4c.5-.5 1.300-.6 1.8-.2l3.1 2.2c.6.4.7 1.3.3 1.9l-1.3 1.8c-.6.8-1.6 1.1-2.5.8C9.8 17.4 5.900 13.3 4.4 7.1c-.2-1 .1-1.9.9-2.5z"/>
        </svg>
      </span>
      <span class="contact-phone">0437 802 615</span>
    </div>

    <div class="photo-circle photo-trainer" role="img" aria-label="Small portrait photo of the personal trainer"></div>
  </main>
</body>
</html>
```